Radiant Harvest Gathering 2021

I am looking to create a flyer for a one day prayer retreat our church is organizing. This flyer will be posted on social media, websites, mobile apps, and will also be printed so it can be mailed to people.

I am looking for something professional, with good use of our logo and band colors (logo colors).

I am counting on the designer's skill, creativity, art and knowledge of media communication to produce a flyer that will effectively and quickly convey the message we are trying to spread.

CONTENT OF THE FLYER:
Event title: Radiant Harvest Gathering
Date: Tuesday July 2nd, 2021
Time: 11:00AM - 7:00PM
Bellmore Hotel, 4817 Wexley Avenue, Portland, Maine 04109 (Room: Tamarind)
Event Key words to highlight what the event is about: Prayer, Fasting, Worship, Prophecy, Revival.
Key phrases:
A one day prayer retreat.
Jesus Chris is Lord

Contact info:
www.quvello.org
Phone: 207 555 0148
Email: contact@brookmeadow.org

```html
<!DOCTYPE html>
<html lang="en">
<head>
<meta charset="utf-8">
<title>Radiant Harvest Gathering 2021</title>
<link rel="stylesheet" href="https://fonts.googleapis.com/css2?family=Oswald:wght@600;700&family=Montserrat:wght@300;400;600;700&display=swap">
<style>
  :root {
    --navy: #0f2130;
    --navy-deep: #0a1822;
    --orange: #f7941d;
    --white: #ffffff;
    --ink: #1b2b3a;
    --rule: rgba(255,255,255,0.75);
  }
  * { margin: 0; padding: 0; box-sizing: border-box; }
  html, body { width: 900px; height: 1200px; overflow: hidden; background: var(--navy-deep); }
  .flyer {
    position: relative; width: 900px; height: 1200px; overflow: hidden;
    font-family: "Montserrat", sans-serif; color: var(--white); text-align: center;
  }
  .flyer__backdrop {
    position: absolute; inset: 0;
    background:
      radial-gradient(ellipse 45% 30% at 78% 78%, rgba(60,110,130,0.35), transparent 70%),
      radial-gradient(ellipse 60% 35% at 40% 82%, rgba(40,80,95,0.35), transparent 70%),
      radial-gradient(ellipse 70% 40% at 70% 20%, rgba(35,70,85,0.35), transparent 75%),
      linear-gradient(180deg, var(--navy) 0%, #112836 55%, var(--navy-deep) 100%);
  }
  .brand { position: absolute; top: 150px; left: 0; right: 0; }
  .brand__name {
    display: inline-flex; align-items: center; gap: 16px;
    font-weight: 600; font-size: 64px; letter-spacing: 2px; color: var(--white);
  }
  .brand__dot { width: 30px; height: 30px; border-radius: 50%; background: var(--orange); }
  .title { position: absolute; top: 320px; left: 0; right: 0; }
  .title__main {
    font-family: "Oswald", sans-serif; font-weight: 700; font-size: 160px; line-height: 1;
    color: var(--orange); letter-spacing: 1px;
  }
  .title__sub { margin-top: 14px; font-weight: 300; font-size: 54px; letter-spacing: 2px; }
  .divider { position: absolute; top: 565px; left: 240px; width: 420px; height: 20px; }
  .when {
    position: absolute; top: 628px; left: 0; right: 0;
    display: flex; justify-content: center; align-items: center; gap: 36px;
  }
  .when__date { display: flex; align-items: center; gap: 10px; }
  .when__day {
    font-family: "Oswald", sans-serif; font-weight: 600; color: var(--orange);
    font-size: 40px; line-height: 0.95; text-align: left;
  }
  .when__year { text-align: left; }
  .when__weekday { font-weight: 700; font-size: 26px; line-height: 1; }
  .when__num { font-weight: 700; font-size: 54px; line-height: 1; }
  .when__sep { width: 2px; height: 80px; background: var(--rule); }
  .when__time { font-weight: 700; font-size: 40px; line-height: 1.05; color: var(--orange); text-align: left; }
  .venue { position: absolute; top: 752px; left: 0; right: 0; font-weight: 600; font-size: 22px; line-height: 1.4; }
  .themes { position: absolute; top: 850px; left: 58px; width: 784px; display: flex; list-style: none; }
  .theme { position: relative; flex: 1; padding-top: 28px; }
  .theme__icon {
    position: absolute; top: 0; left: 50%; transform: translateX(-50%);
    width: 66px; height: 66px; border-radius: 50%; background: var(--orange);
    border: 4px solid var(--white); display: flex; align-items: center; justify-content: center; z-index: 1;
  }
  .theme__label {
    background: var(--white); color: var(--ink); font-weight: 700; font-size: 24px;
    height: 96px; padding-top: 52px; border-right: 3px solid #c9d0d6;
  }
  .theme:last-child .theme__label { border-right: none; }
  .slogan {
    position: absolute; top: 1010px; left: 0; right: 0;
    font-weight: 700; font-size: 29px; color: var(--orange); letter-spacing: 0.5px;
  }
  .contacts {
    position: absolute; top: 1088px; left: 0; right: 0;
    display: grid; grid-template-columns: 269px 345px 286px; align-items: center;
  }
  .contact {
    display: flex; flex-direction: column; align-items: center; gap: 14px;
    font-weight: 600; font-size: 17px; height: 66px; justify-content: flex-end;
  }
  .contact--mid { border-left: 2px solid var(--rule); border-right: 2px solid var(--rule); }
  .contact__icon { width: 32px; height: 32px; border-radius: 50%; background: var(--white); display: flex; align-items: center; justify-content: center; }
</style>
</head>
<body>
<main class="flyer">
  <div class="flyer__backdrop" role="img" aria-label="Dim background photo of an open bible and a lit candle in dark blue tones"></div>

  <header class="brand">
    <div class="brand__name"><span class="brand__dot"></span>VERANTH</div>
  </header>

  <section class="title">
    <h1 class="title__main">RADIANT</h1>
    <p class="title__sub">HARVEST GATHERING</p>
  </section>

  <svg class="divider" viewBox="0 0 420 20" aria-hidden="true">
    <line x1="0" y1="2" x2="420" y2="2" stroke="#fff" stroke-width="2"/>
    <polygon points="198,2 222,2 210,16" fill="#fff"/>
  </svg>

  <section class="when">
    <div class="when__date">
      <div class="when__day">2ND<br>JULY</div>
      <div class="when__year"><div class="when__weekday">TUESDAY</div><div class="when__num">2021</div></div>
    </div>
    <div class="when__sep"></div>
    <div class="when__time">11:00AM-<br>7:00PM</div>
  </section>

  <p class="venue">Bellmore Hotel, 4817 Wexley Avenue, Portland,<br>Maine 04109 (Room: Tamarind)</p>

  <ul class="themes">
    <li class="theme"><span class="theme__icon"><svg width="34" height="34" viewBox="0 0 34 34"><path d="M17 4 L11 20 L8 30 H15 L17 18 L19 30 H26 L23 20 Z" fill="#fff"/></svg></span><div class="theme__label">Prayer</div></li>
    <li class="theme"><span class="theme__icon"><svg width="34" height="34" viewBox="0 0 34 34" fill="#fff"><rect x="8" y="4" width="2" height="10"/><rect x="12" y="4" width="2" height="10"/><rect x="16" y="4" width="2" height="10"/><rect x="11" y="12" width="4" height="18" rx="2"/><path d="M22 4 C28 6 28 16 24 18 V30 H21 V4Z"/></svg></span><div class="theme__label">Fasting</div></li>
    <li class="theme"><span class="theme__icon"><svg width="34" height="34" viewBox="0 0 34 34"><rect x="6" y="6" width="22" height="22" rx="2" fill="none" stroke="#fff" stroke-width="3"/><path d="M17 6 V28" stroke="#fff" stroke-width="2"/><path d="M10 12 H14 M10 17 H14 M20 12 H24 M20 17 H24" stroke="#fff" stroke-width="2"/></svg></span><div class="theme__label">Worship</div></li>
    <li class="theme"><span class="theme__icon"><svg width="34" height="34" viewBox="0 0 34 34"><circle cx="17" cy="17" r="12" fill="none" stroke="#fff" stroke-width="3"/><circle cx="17" cy="17" r="5" fill="#fff"/></svg></span><div class="theme__label">Prophecy</div></li>
    <li class="theme"><span class="theme__icon"><svg width="34" height="34" viewBox="0 0 34 34"><path d="M17 4 C24 12 26 18 22 26 C20 30 14 30 12 26 C9 20 12 14 17 4Z" fill="#fff"/></svg></span><div class="theme__label">Revival</div></li>
  </ul>

  <p class="slogan">A ONE DAY PRAYER RETREAT JESUS CHRIS IS LORD</p>

  <footer class="contacts">
    <div class="contact"><span class="contact__icon"><svg width="18" height="18" viewBox="0 0 18 18"><path d="M4 2 L7 2 L8 6 L6 7.5 C7 10 8 11 10.5 12 L12 10 L16 11 L16 14 C16 15 15 16 14 16 C8 16 2 10 2 4 C2 3 3 2 4 2Z" fill="#0f2130"/></svg></span>207 555 0148</div>
    <div class="contact contact--mid"><span class="contact__icon"><svg width="18" height="18" viewBox="0 0 18 18"><rect x="2" y="4" width="14" height="10" rx="1" fill="#0f2130"/><path d="M2.5 4.5 L9 10 L15.5 4.5" stroke="#fff" stroke-width="1.4" fill="none"/></svg></span>contact@brookmeadow.org</div>
    <div class="contact"><span class="contact__icon"><svg width="18" height="18" viewBox="0 0 18 18" fill="none" stroke="#0f2130" stroke-width="1.6"><circle cx="9" cy="9" r="7"/><ellipse cx="9" cy="9" rx="3" ry="7"/><path d="M2 9 H16"/></svg></span>www.quvello.org</div>
  </footer>
</main>
</body>
</html>
```